KORVEL Group Pty Ltd. Website and Domain

www.korvelgroup.com.au

require email addresses setup.

Info@korvelgroup.com.au
accounts@korvelgroup.com.au
peter.walsby@korvelgroup.com.au
roland.hughes@korvelgroup.com.au

Website should promote commercial and domestic electrical services, audio visual services and data and fibre installations.

similar to my mates site www.bvplanet.com.au

Website needs to promote professionalism, electrical/electrician, audio visual and data/fibre cabling installations.

promote environmental friendly imaginary.

```html
<!DOCTYPE html>
<html lang="en">
<head>
<meta charset="utf-8">
<title>KORVEL Group Pty Ltd.</title>
<link href="https://fonts.googleapis.com/css2?family=Montserrat:wght@300;400;500;600;700&display=swap" rel="stylesheet">
<style>
:root{
  --blue:#2eaadf;
  --green:#a9cf46;
  --ink:#1c1c1c;
  --text:#7a7a7a;
  --white:#ffffff;
  --field:#ffffff;
}
*{box-sizing:border-box;margin:0;padding:0}
html,body{width:1200px;height:3907px;overflow:hidden;background:var(--white)}
body{position:relative;font-family:'Montserrat',sans-serif;color:var(--ink)}
.abs{position:absolute}

/* header */
.site-header{position:absolute;left:0;top:0;width:1200px;height:94px;background:var(--white);border-top:3px solid var(--green);z-index:3}
.brand{position:absolute;left:144px;top:18px;display:flex;align-items:center;gap:10px}
.brand-dot{width:56px;height:56px;border-radius:50%;border:4px solid var(--green);flex:none}
.brand-name{font-size:18px;font-weight:600;color:var(--blue);letter-spacing:0.5px;white-space:nowrap}
.main-nav a{position:absolute;top:38px;font-size:14px;font-weight:500;color:var(--ink);text-decoration:none}
.main-nav a.active::after{content:"";position:absolute;left:-4px;right:-4px;bottom:-9px;height:3px;background:var(--green)}
.social{position:absolute;width:36px;height:36px;border-radius:50%;background:var(--blue)}

/* hero */
.hero{position:absolute;left:0;top:94px;width:1200px;height:763px;background:linear-gradient(180deg,#1a1d2a 0%,#2b2630 40%,#6a4320 70%,#3a2a1c 100%)}
.hero-title{position:absolute;left:0;width:1200px;top:190px;text-align:center;font-size:58px;font-weight:700;line-height:62px;color:var(--white);letter-spacing:1px}
.hero-sub{position:absolute;left:0;width:1200px;top:350px;text-align:center;font-size:21px;font-weight:500;color:var(--white)}
.btn{position:absolute;display:flex;align-items:center;justify-content:center;background:var(--green);color:var(--white);font-weight:600;border-radius:31px;text-transform:uppercase;font-size:17px;text-decoration:none}
.dots{position:absolute;top:600px;left:561px;display:flex;gap:7px}
.dots span{width:10px;height:10px;border-radius:50%;background:var(--white)}
.dots span.on{background:var(--green)}

/* welcome */
.section-title{position:absolute;left:0;width:1200px;text-align:center;font-size:40px;font-weight:700;color:var(--ink)}
.section-title .light{font-weight:400}
.c-blue{color:var(--blue)}.c-green{color:var(--green)}
.welcome-text{position:absolute;left:160px;width:880px;top:1010px;text-align:center;font-size:16px;line-height:32px;color:var(--text)}

/* photo band */
.room-photo{position:absolute;left:0;top:1259px;width:1200px;height:658px;background:linear-gradient(180deg,#e9ecef 0%,#d8dbe0 45%,#6a65a8 75%,#4a4652 100%)}

/* services */
.service{position:absolute;width:285px;text-align:center}
.service-img{width:285px}
.service h3{font-size:21px;font-weight:500;line-height:28px;margin-top:30px;color:var(--ink)}
.service p{font-size:13px;line-height:21px;color:var(--text);margin-top:17px;padding:0 10px}

/* contact */
.contact{position:absolute;left:0;top:2847px;width:1200px;height:780px;background:linear-gradient(135deg,#3bb0e2 0%,#2ea6dc 60%,#34abe0 100%)}
.contact .section-title{color:var(--white)}
.field{position:absolute;background:var(--field);border-radius:2px;font-size:14px;color:#555;padding:17px 22px}

/* footer */
.footer-nav a{position:absolute;top:3744px;font-size:19px;font-weight:500;color:var(--ink);text-decoration:none}
.copyright{position:absolute;left:0;width:1200px;top:3798px;text-align:center;font-size:13px;color:#555}
</style>
</head>
<body>

<header class="site-header">
  <div class="brand"><span class="brand-dot"></span><span class="brand-name">KORVEL Group Pty Ltd.</span></div>
  <nav class="main-nav">
    <a class="active" style="left:472px" href="#">HOME</a>
    <a style="left:555px" href="#">ABOUT US</a>
    <a style="left:667px" href="#">SERVICES</a>
    <a style="left:775px" href="#">NEWS</a>
    <a style="left:857px" href="#">CONTACT US</a>
  </nav>
  <span class="social" style="left:976px;top:28px" aria-label="Social link"></span>
  <span class="social" style="left:1018px;top:28px" aria-label="Social link"></span>
</header>

<section class="hero" role="img" aria-label="House at night decorated with warm festive lights">
  <h1 class="hero-title">COMPLETE PACKAGE<br>SOLUTIONS</h1>
  <p class="hero-sub">Electrical, Audio Visual and Data services</p>
  <a class="btn" style="left:505px;top:420px;width:190px;height:61px">Get Started</a>
  <div class="dots"><span></span><span></span><span class="on"></span><span></span><span></span></div>
  <svg class="abs" style="left:0;top:600px" width="1200" height="163" viewBox="0 0 1200 163">
    <path d="M0 58 C 120 128, 220 143, 330 136 C 500 118, 700 -4, 910 -4 C 1040 -4, 1130 38, 1200 73 L1200 163 L0 163 Z" fill="var(--green)"/>
    <path d="M0 69 C 120 139, 220 154, 330 147 C 500 129, 700 7, 910 7 C 1040 7, 1130 49, 1200 84 L1200 163 L0 163 Z" fill="var(--blue)"/>
    <path d="M0 80 C 120 150, 220 165, 330 158 C 500 140, 700 18, 910 18 C 1040 18, 1130 60, 1200 95 L1200 163 L0 163 Z" fill="var(--white)"/>
  </svg>
</section>

<h2 class="section-title" style="top:920px">WELCOMR TO <span class="light c-blue">KORVEL</span> <span class="light c-green">GROUP</span></h2>
<p class="welcome-text">Lorem ipsum dolor sit amet, consectetur adipiscing elit, sed do eiusmod tempor incididunt ut labore et dolore magna uis ipsum suspendisse ultrices grcommodo viverra maecenas accumsan lacus vel facilisis. Lorem ipsum dolor sit amet, consectetur adipiscing elit, sed do eiusmod tempor incididunt ut labore et dolore magna uis ipsum suspendisse ultrices grcommodo viverra maecenas accumsan lacus vel facilisis. Lorem ipsum dolor sit amet, consectetur adipiscing elit, sed do eiusmod tempor incididunt ut labore et dolore magna uis ipsum suspendisse ultrices grcommodo viverra maecenas accumsan lacus vel facilisis.</p>

<div class="room-photo" role="img" aria-label="Conference room with monitor, microphone and rows of chairs"></div>
<svg class="abs" style="left:0;top:1250px" width="1200" height="110" viewBox="0 0 1200 110">
  <path d="M0 0 L1200 0 L1200 25 C 1050 -5, 900 5, 780 30 C 650 58, 560 95, 480 70 C 330 20, 150 10, 0 75 Z" fill="var(--white)"/>
  <path d="M50 72 C 150 40, 270 26, 370 32 C 460 36, 530 60, 560 82 C 470 96, 420 58, 300 55 C 200 52, 110 70, 50 72 Z" fill="var(--green)"/>
</svg>

<h2 class="section-title" style="top:2015px">OUR <span class="light c-blue">SERVICES</span></h2>

<div class="service" style="left:144px;top:2165px">
  <div class="service-img" role="img" aria-label="Modern house exterior at dusk" style="height:268px;background:linear-gradient(180deg,#2e3a3c,#5a6a5c 60%,#3d5a22)"></div>
  <h3>Electrical<br>Services</h3>
  <p>Lorem ipsum dolor sit ameconsectetur adipiscing elit, sed do eiusmod tempor incididunt ut labore et dolore magna aluspendisse ultrices gravida</p>
</div>
<div class="service" style="left:458px;top:2127px">
  <div class="service-img" role="img" aria-label="Microphone on stand in front of an auditorium" style="height:306px;background:linear-gradient(180deg,#8a5a3c,#b37850 45%,#4a3a3c)"></div>
  <h3>Audio Visual<br>Services</h3>
  <p>Lorem ipsum dolor sit ameconsectetur adipiscing elit, sed do eiusmod tempor incididunt ut labore et dolore magna aluspendisse ultrices gravida</p>
</div>
<div class="service" style="left:771px;top:2165px">
  <div class="service-img" role="img" aria-label="Blue network cables plugged into a patch panel" style="height:268px;background:linear-gradient(135deg,#d9dde2,#7fa8c8 45%,#2a66b0)"></div>
  <h3>DATA and sustainable<br>Practices</h3>
  <p>Lorem ipsum dolor sit ameconsectetur adipiscing elit, sed do eiusmod tempor incididunt ut labore et dolore magna aluspendisse ultrices gravida</p>
</div>

<a class="btn" style="left:463px;top:2693px;width:273px;height:61px">View More Services</a>

<section class="contact" role="img" aria-label="Technicians working, tinted blue">
  <h2 class="section-title" style="top:98px">CONTACT <span class="light">FORM</span></h2>
  <div class="field" style="left:234px;top:200px;width:359px;height:52px">First Name</div>
  <div class="field" style="left:605px;top:200px;width:360px;height:52px">Last Name</div>
  <div class="field" style="left:234px;top:266px;width:359px;height:52px">Email address</div>
  <div class="field" style="left:605px;top:266px;width:360px;height:52px">Phone Number</div>
  <div class="field" style="left:234px;top:331px;width:731px;height:112px">Message</div>
  <a class="btn" style="left:463px;top:487px;width:273px;height:61px">Submit Message</a>
  <svg class="abs" style="left:0;top:620px" width="1200" height="160" viewBox="0 0 1200 160">
    <path d="M0 78 C 200 150, 390 145, 560 95 C 760 20, 1000 25, 1200 95 L1200 110 C 1000 40, 760 35, 560 110 C 390 160, 200 165, 0 92 Z" fill="var(--green)"/>
    <path d="M0 92 C 200 165, 390 160, 560 110 C 760 35, 1000 40, 1200 110 L1200 122 C 1000 52, 760 47, 560 122 C 390 172, 200 177, 0 104 Z" fill="var(--blue)"/>
    <path d="M0 104 C 200 177, 390 172, 560 122 C 760 47, 1000 52, 1200 122 L1200 160 L0 160 Z" fill="var(--white)"/>
  </svg>
</section>

<div class="brand" style="left:458px;top:3632px"><span class="brand-dot" style="width:72px;height:72px"></span><span class="brand-name" style="font-size:34px">KORVEL</span></div>

<nav class="footer-nav">
  <a style="left:294px" href="#">HOME</a>
  <a style="left:400px" href="#">ABOUT US</a>
  <a style="left:544px" href="#">SERVICES</a>
  <a style="left:683px" href="#">NEWS</a>
  <a style="left:787px" href="#">CONTACT US</a>
</nav>
<p class="copyright">© 2020 Korvel Group.All Rights reserved &nbsp;|&nbsp; Privacy Policy</p>
<span class="social" style="left:561px;top:3841px" aria-label="Social link"></span>
<span class="social" style="left:603px;top:3841px" aria-label="Social link"></span>

</body>
</html>
```